Farrow Fundraising E-mail Campaign

I intend to use Constant Contact to send donors 4 separate e-mail messages with pictures, text and a hot link, “Give to Help Restore Pinewick.” E-mails will spaced about 3 days apart. I would like the first e-mail to go out on Monday, December 17. The e-mail campaign is part of a board match annual appeal fundraising campaign for a not for profit sleep away Christian camp. Our hope is to raise $40,000.00+

Target Market(s)

Members in Constant Contact list

Colors

Designer to choose colors to be used in the design.

Requirements
Must have
• E- mail recipient must be able to access hot link

```html
<!DOCTYPE html>
<html lang="en">
<head>
<meta charset="utf-8">
<title>Farrow Camp Appeal Email</title>
<link rel="stylesheet" href="https://fonts.googleapis.com/css2?family=Arimo:ital,wght@0,400;0,700;1,700&display=swap">
<style>
  :root {
    --page-bg: #ffffff;
    --ink: #111111;
    --link: #0000ee;
    --photo-dark: #2a211c;
    --photo-mid: #5c4a3a;
    --photo-light: #9fb07a;
  }
  * { box-sizing: border-box; margin: 0; padding: 0; }
  html, body {
    width: 1200px;
    height: 812px;
    overflow: hidden;
    background: var(--page-bg);
  }
  body {
    font-family: "Arimo", Arial, sans-serif;
    color: var(--ink);
  }
  .email {
    position: absolute;
    left: 300px;
    top: 29px;
    width: 584px;
  }
  .hero-photo {
    display: block;
    width: 580px;
    height: 419px;
    margin-left: 2px;
    background:
      radial-gradient(ellipse 38% 55% at 62% 52%, var(--photo-mid), transparent 70%),
      linear-gradient(90deg, var(--photo-light) 0%, var(--photo-dark) 38%, var(--photo-dark) 80%, var(--photo-light) 100%);
  }
  .body-copy {
    font-size: 12.2px;
    line-height: 17.2px;
    margin-top: 10px;
  }
  .body-copy + .body-copy { margin-top: 11px; }
  .match-pledge {
    font-weight: 700;
    font-style: italic;
    font-size: 13.2px;
    line-height: 18px;
  }
  .call-to-action { margin-top: 18px; }
  .give-line {
    font-size: 13.6px;
    line-height: 18px;
    margin-top: 13px;
  }
  .give-link {
    color: var(--link);
    font-weight: 700;
    text-decoration: underline;
  }
</style>
</head>
<body>
  <main class="email">
    <div class="hero-photo" role="img" aria-label="Smiling teenage camper in a cap with sunglasses, inside a dim lodge with bright windows behind"></div>

    <p class="body-copy">Unfortunately, too many of our children spend more time playing video games and watching TV than having fun playing outdoors. Mateo, an average 13-year-old, spends about 300 hours a year playing video games. That’s because many parents wonder where they can find a safe and engaging place for their children to experience nature and engaging activities with peers.</p>

    <p class="body-copy">The Board of Directors of Farrow Presbyterian Camp and Conference Center decided to create a space that is safe, meaningful and fun by issuing the Revitalize Camp Pinewick Lake Matching Challenge. <span class="match-pledge">They will match on a 1: 1 basis every dollar given or pledged to the campaign by December 31 up to $20,000.00.</span></p>

    <p class="body-copy call-to-action">Please help us create a space where children like Mateo experience nature, connect with other children and have fun! Take advantage of the Revitalize Camp Pinewick Lake Matching Challenge and donate today.</p>

    <p class="give-line">Click here to <a class="give-link" href="#">Give to Help Restore Pinewick</a> and choose "Restore Pinewick"</p>
  </main>
</body>
</html>
```